" Nós fazemos a administração geral dos condomínios. O que envolve solução de conflitos, contratação de serviços, orçamentos, administração financeira, reuniões de condôminos, relatórios gerenciais, orientações diversas ao síndico, conselheiros e condôminos. "

```html
<!DOCTYPE html>
<html lang="pt-BR">
<head>
<meta charset="UTF-8">
<title>Papel timbrado — Altamura</title>
<link href="https://fonts.googleapis.com/css2?family=Montserrat:wght@400;500;700&display=swap" rel="stylesheet">
<style>
  :root {
    --navy: #1d3f6e;
    --sky: #3aa3d8;
    --ink: #23364f;
    --paper: #ffffff;
    --backdrop: #eceef0;
  }
  html, body {
    margin: 0;
    padding: 0;
    width: 1200px;
    height: 1200px;
    overflow: hidden;
    background: var(--backdrop);
    font-family: "Montserrat", Arial, sans-serif;
  }
  .letterhead {
    position: absolute;
    left: 210px;
    top: 48px;
    width: 780px;
    height: 1104px;
    background: var(--paper);
    overflow: hidden;
  }
  .brand {
    position: absolute;
    right: 428px;
    top: 104px;
    display: flex;
    align-items: center;
    gap: 10px;
    white-space: nowrap;
  }
  .brand-square {
    width: 20px;
    height: 20px;
    background: var(--sky);
    flex: none;
  }
  .brand-name {
    font-size: 24px;
    font-weight: 700;
    letter-spacing: 1px;
    color: var(--navy);
    line-height: 1;
  }
  .header-divider {
    position: absolute;
    left: 372px;
    top: 30px;
    width: 3px;
    height: 128px;
    background: var(--navy);
  }
  .contact {
    position: absolute;
    left: 394px;
    top: 34px;
    margin: 0;
    padding: 0;
    list-style: none;
    font-size: 15px;
    font-weight: 400;
    color: var(--ink);
    line-height: 20px;
    white-space: nowrap;
  }
  .contact .web { margin-top: 24px; }
  .contact .mail { margin-top: 18px; }
  .footer-mark {
    position: absolute;
    left: 40px;
    top: 970px;
    width: 56px;
    height: 56px;
    background: var(--sky);
  }
  .footer-rule {
    position: absolute;
    left: 96px;
    right: 0;
    top: 1000px;
    height: 7px;
    background: var(--navy);
  }
</style>
</head>
<body>
  <main class="letterhead">
    <div class="brand">
      <span class="brand-square"></span>
      <span class="brand-name">ALTAMURA</span>
    </div>
    <div class="header-divider"></div>
    <ul class="contact">
      <li>(11) 4210-3380</li>
      <li>(11) 9 4821-6097</li>
      <li class="web">www.altamura.com.br</li>
      <li class="mail">contato@altamura.com.br</li>
    </ul>
    <div class="footer-mark"></div>
    <div class="footer-rule"></div>
  </main>
</body>
</html>
```